Bref créative
Biz Card for a Professional Organizer
Dana Kowalt
Cutting-Edge
Room Clearing Maestro
Serving the North Coast
info@42plumova.com
www.42plumova.com
I'd like a clean design, possibly going vertical instead of the traditional horizontal-UNLESS it is just going to look better going horizontal.
I'm open to suggestions here. I also have black and white versions of my logo if that would work well here...
black version of logo
reverse version of logo
color version

```html
<!DOCTYPE html>
<html lang="en">
<head>
<meta charset="utf-8">
<title>42 Plumova – Business Card</title>
<link href="https://fonts.googleapis.com/css2?family=Ubuntu:wght@400;500;700&display=swap" rel="stylesheet">
<style>
  :root {
    --page: #e9e4dc;
    --white: #ffffff;
    --teal: #3f8ca6;
    --teal-deep: #2b6b83;
    --teal-light: #5aa3bb;
    --brown: #7b5238;
  }
  * { box-sizing: border-box; margin: 0; padding: 0; }
  html, body { width: 1200px; height: 866px; overflow: hidden; }
  body {
    background: var(--page);
    font-family: "Ubuntu", sans-serif;
    position: relative;
  }
  .card {
    position: absolute;
    top: 48px;
    width: 403px;
    height: 655px;
    overflow: hidden;
    box-shadow: 0 6px 18px rgba(0,0,0,0.18);
  }
  .card--front { left: 77px; background: var(--white); }
  .card--back {
    left: 672px;
    background: radial-gradient(ellipse at 50% 45%, var(--teal-light) 0%, var(--teal) 50%, var(--teal-deep) 100%);
  }
  .card__wave { position: absolute; inset: 0; width: 100%; height: 100%; }

  .brand { position: absolute; top: 92px; left: 0; right: 0; text-align: center; }
  .brand__name {
    color: var(--teal);
    font-weight: 700;
    font-size: 46px;
    letter-spacing: 1px;
    line-height: 1;
  }
  .brand__tagline {
    margin-top: 22px;
    color: var(--teal);
    font-size: 17px;
    line-height: 1.15;
  }
  .brand__tagline span { display: block; letter-spacing: 5px; }

  .person {
    position: absolute; top: 458px; left: 0; right: 0;
    text-align: center; color: var(--white);
  }
  .person__name { font-weight: 700; font-size: 15px; }
  .person__role { font-size: 12px; margin-top: 5px; }

  .contact {
    position: absolute; top: 544px; left: 110px;
    list-style: none; color: var(--white); font-size: 12px;
  }
  .contact li { display: flex; align-items: center; height: 21px; }
  .contact svg { width: 12px; height: 12px; margin-right: 7px; flex: none; }

  .back-mark {
    position: absolute; top: 118px; left: 0; right: 0; text-align: center;
    color: rgba(255,255,255,0.13);
    font-weight: 700; font-size: 46px; letter-spacing: 1px;
  }
  .back-url {
    position: absolute; top: 612px; left: 0; right: 0; text-align: center;
    color: var(--white); font-size: 13px; letter-spacing: 5px;
  }
</style>
</head>
<body>
  <section class="card card--front">
    <svg class="card__wave" viewBox="0 0 403 655" preserveAspectRatio="none" aria-hidden="true">
      <defs>
        <linearGradient id="frontTeal" x1="0" y1="0" x2="0" y2="1">
          <stop offset="0" stop-color="#5aa3bb"/>
          <stop offset="1" stop-color="#2f7189"/>
        </linearGradient>
      </defs>
      <path d="M0,340 C110,312 260,290 403,300 L403,655 L0,655 Z" fill="url(#frontTeal)"/>
      <path d="M0,316 C100,292 250,262 403,270 C280,276 140,304 0,336 Z" fill="var(--brown)"/>
    </svg>

    <div class="brand">
      <div class="brand__name">42 PLUMOVA</div>
      <p class="brand__tagline">Mindful Decluttering<span>services</span></p>
    </div>

    <div class="person">
      <h1 class="person__name">Dana Kowalt</h1>
      <p class="person__role">Room Clearing Maestro</p>
    </div>

    <ul class="contact">
      <li><svg viewBox="0 0 12 12"><circle cx="6" cy="6" r="6" fill="#fff"/><path d="M6 2.5a2 2 0 0 0-2 2c0 1.5 2 4 2 4s2-2.5 2-4a2 2 0 0 0-2-2z" fill="var(--teal)"/></svg>Serving the North Coast</li>
      <li><svg viewBox="0 0 12 12"><circle cx="6" cy="6" r="6" fill="#fff"/><path d="M4 3h1.2l.6 1.6-.8.6a4 4 0 0 0 1.8 1.8l.6-.8L9 6.8V8a1 1 0 0 1-1 1A5 5 0 0 1 3 4a1 1 0 0 1 1-1z" fill="var(--teal)"/></svg>(415) 555-0142</li>
      <li><svg viewBox="0 0 12 12"><circle cx="6" cy="6" r="6" fill="#fff"/><rect x="3" y="4" width="6" height="4" fill="var(--teal)"/><path d="M3 4l3 2.2L9 4" stroke="#fff" stroke-width="0.7" fill="none"/></svg>info@42plumova.com</li>
      <li><svg viewBox="0 0 12 12"><circle cx="6" cy="6" r="6" fill="#fff"/><circle cx="6" cy="6" r="3.2" fill="none" stroke="var(--teal)" stroke-width="0.8"/><path d="M2.8 6h6.4M6 2.8c-1.4 1.8-1.4 4.6 0 6.4M6 2.8c1.4 1.8 1.4 4.6 0 6.4" stroke="var(--teal)" stroke-width="0.7" fill="none"/></svg>www.42plumova.com</li>
    </ul>
  </section>

  <section class="card card--back">
    <div class="back-mark">42 PLUMOVA</div>
    <p class="back-url">www.42plumova.com</p>
  </section>
</body>
</html>
```